Bref créative
Church stationary, door hangers, envelopes (large & small), and banner
Harvest Light Fellowship
We are a church concerned with our community, interested in reaching out to them with the love of God.
Religion and Spirituality
A.) Business card and stationery:
The envelope sizes are the standard #10 letter envelope and the standard large envelope size that a 8 1/2" x 11" piece of paper can fit into.
Please present designs with the current logo image that we have uploaded. Notice there are two styles, one with the church name in the logo and one image without it. Our current business card uses the logo image with the name of the church in it. We want to see designs using both logo images.
Name on business card: Dwight L. Barlow
Designation: Pastor
Business address: 2738 Kessler Mill Rd.
Phone numbers:
803-628-xxxx cell (we can add this number later)
803-472-1958 office
E-mail and website:
pastor@harvestlightfw.org
www.harvestlightfw.org
B.) Door hanger:
The door hanger size is approximately 4 1/2" wide x 12" tall.
Sample is attached. The back side should contain a map showing the directions to the church, service times, and a simple message inviting them to church
C.) Banner:
This should be a horizontal banner to be printed on a vinyl sign approximately 3' x 5'.
Include Tagline: Sunday 3:00 pm, Wednesday 7:30 pm
The image will be the church logo and name of the church. Also, included on the sign will be the times of the services, listed above. We are looking at using a white background for this sign.
Please see scanned image of our current business card layout. We want to see the business card presented with the name "Harvest Light" as part of the image and apart and to the right of the image. Thanks for your designs.
This is our current stationary.
We have uploaded a zip file with the logo vector files i.e. eps files. Hope this helps.
Thanks,
TM
Door hanger sample

```html
<!DOCTYPE html>
<html lang="en">
<head>
<meta charset="utf-8">
<title>Harvest Light Fellowship – Stationery</title>
<link href="https://fonts.googleapis.com/css2?family=Marcellus&family=Cinzel:wght@400;600&family=Lato:wght@400&display=swap" rel="stylesheet">
<style>
  :root{
    --board:#8a5630;
    --paper:#ffffff;
    --teal:#17767d;
    --teal-dark:#0f5a60;
    --gold:#b8892b;
    --mark:#c9a75a;
    --ink:#333333;
    --label:#ffffff;
  }
  html,body{margin:0;padding:0;overflow:hidden}
  body{width:1200px;height:778px;background:var(--board);position:relative;font-family:"Lato",sans-serif}
  .piece{position:absolute;background:var(--paper);box-shadow:0 3px 10px rgba(0,0,0,.35);overflow:hidden}
  .piece svg.band{position:absolute;left:0;bottom:0;display:block}
  .mark{background:var(--mark);position:absolute}
  .church-name{font-family:"Marcellus",serif;color:var(--gold);position:absolute;white-space:nowrap}
  .band-text{position:absolute;left:0;right:0;text-align:center;color:#fff;font-family:"Lato",sans-serif}

  /* Letterhead */
  .letterhead{left:0;top:7px;width:564px;height:766px}
  .letterhead .mark{left:250px;top:54px;width:86px;height:98px}
  .letterhead .church-name{left:0;right:0;text-align:center;top:160px;font-size:22px}
  .letterhead .addr{bottom:46px;font-size:11px}
  .letterhead .contact{bottom:24px;font-size:15px}

  /* Label */
  .set-label{position:absolute;left:792px;top:152px;color:var(--label);font-family:"Lato",sans-serif;font-size:19px;letter-spacing:.5px}

  /* Business cards */
  .card{top:259px;width:230px;height:125px}
  .card-front{left:636px}
  .card-back{left:883px}
  .card svg{position:absolute;inset:0}
  .card-front .mark{left:82px;top:16px;width:30px;height:40px}
  .card-front .person{position:absolute;left:0;right:0;top:60px;text-align:center;font-family:"Cinzel",serif;font-size:10px;color:var(--ink)}
  .card-front .details{position:absolute;left:0;right:0;top:76px;text-align:center;font-size:5.5px;line-height:8px;color:var(--ink)}
  .card-back .mark{left:99px;top:34px;width:30px;height:36px}
  .card-back .church-name{left:0;right:0;text-align:center;top:78px;font-size:12px}
  .card-caption{position:absolute;top:396px;width:230px;text-align:center;color:var(--label);font-size:12px}

  /* Envelope */
  .envelope{left:571px;top:449px;width:622px;height:324px}
  .envelope .mark{left:12px;top:12px;width:34px;height:44px}
  .envelope .church-name{left:12px;top:60px;font-size:7px}
  .envelope .addr{bottom:42px;font-size:9px}
  .envelope .contact{bottom:22px;font-size:13px}
</style>
</head>
<body>

<section class="piece letterhead">
  <div class="mark"></div>
  <div class="church-name">Harvest Light Fellowship</div>
  <svg class="band" width="564" height="110" viewBox="0 0 564 110">
    <path d="M0,40 Q282,-4 564,40 L564,110 L0,110 Z" fill="var(--teal)"/>
    <path d="M0,30 Q282,-14 564,30" fill="none" stroke="var(--teal-dark)" stroke-width="2"/>
    <path d="M0,50 Q282,8 564,50" fill="none" stroke="#fff" stroke-width="2"/>
  </svg>
  <div class="band-text addr">2738 Kessler Mill Road, West Columbia, SC 29170</div>
  <div class="band-text contact">(803) 472-1958 &nbsp;|&nbsp; www.harvestlightfw.org</div>
</section>

<div class="set-label">STATIONARY #10</div>

<section class="piece card card-front">
  <svg width="230" height="125" viewBox="0 0 230 125">
    <path d="M0,0 L16,0 Q4,62 16,125 L0,125 Z" fill="var(--teal)"/>
    <path d="M20,0 Q8,62 20,125" fill="none" stroke="var(--teal)" stroke-width="1.5"/>
  </svg>
  <div class="mark"></div>
  <div class="person">Rev. Dwight Barlow, Pastor</div>
  <div class="details">2738 Kessler Mill Road, West Columbia, SC 29170<br>Phone: (803) 472-1958<br>Email: pastor@harvestlightfw.org<br>Website: www.harvestlightfw.org</div>
</section>
<div class="card-caption" style="left:636px">Front</div>

<section class="piece card card-back">
  <svg width="230" height="125" viewBox="0 0 230 125">
    <path d="M0,0 L16,0 Q4,62 16,125 L0,125 Z" fill="var(--teal)"/>
    <path d="M230,0 L214,0 Q226,62 214,125 L230,125 Z" fill="var(--teal)"/>
  </svg>
  <div class="mark"></div>
  <div class="church-name">Harvest Light Fellowship</div>
</section>
<div class="card-caption" style="left:883px">Back</div>

<section class="piece envelope">
  <div class="mark"></div>
  <div class="church-name">Harvest Light Fellowship</div>
  <svg class="band" width="622" height="90" viewBox="0 0 622 90">
    <path d="M0,34 Q311,-6 622,34 L622,90 L0,90 Z" fill="var(--teal)"/>
    <path d="M0,44 Q311,6 622,44" fill="none" stroke="#fff" stroke-width="2"/>
  </svg>
  <div class="band-text addr">2738 Kessler Mill Road, West Columbia, SC 29170</div>
  <div class="band-text contact">(803) 472-1958 &nbsp;|&nbsp; www.harvestlightfw.org</div>
</section>

</body>
</html>
```